Business Card Design

Cedar Gate Rentals
Cedar Gate Rentals is a high end home rental leasing company that provides exquisite properties in niche markets. We are a small family owned business that considers our clients not as renters, but as friends. Every property we buy must be brought up to our high standards before it is offered on the market. The properties that we lease are exceptional, "move in" ready homes. This allows for the client to take pride in their lease as if it was their own home. To put it another way; we do not lease a property that we would not live in ourselves.

Target Market(s)

Couples making $100K or more

Industry/Entity Type

Business

Requirements
Must have
• Some sort of logo
Nice to have
• good slogan
Should not have
• Pink

```html
<!DOCTYPE html>
<html lang="en">
<head>
<meta charset="utf-8">
<title>Cedar Gate Rentals – Business Card</title>
<link rel="stylesheet" href="https://fonts.googleapis.com/css2?family=Arimo:wght@400;700&display=swap">
<style>
  :root {
    --lime: #cde05e;
    --sky: #6dcdf5;
    --ink: #5b5b5b;
    --paper: #ffffff;
  }
  html, body {
    margin: 0;
    padding: 0;
    width: 1200px;
    height: 704px;
    overflow: hidden;
    background: var(--paper);
  }
  .card {
    position: relative;
    width: 1200px;
    height: 704px;
    background: var(--paper);
    font-family: "Arimo", Arial, sans-serif;
    line-height: 1;
  }
  .top-band {
    position: absolute;
    left: 0; top: 0;
    width: 100%; height: 24px;
    background: var(--lime);
  }
  .brand-mark {
    position: absolute;
    left: 130px; top: 80px;
    width: 166px; height: 166px;
    background: var(--sky);
  }
  .brand-name {
    position: absolute;
    left: 316px; top: 118px;
    margin: 0;
    font-size: 46px;
    font-weight: 700;
    color: var(--lime);
    letter-spacing: 0.2px;
  }
  .slogan {
    position: absolute;
    left: 316px; top: 180px;
    margin: 0;
    font-size: 30px;
    font-weight: 400;
    color: var(--sky);
  }
  .person-name {
    position: absolute;
    left: 130px; top: 373px;
    margin: 0;
    font-size: 39px;
    font-weight: 400;
    color: var(--sky);
  }
  .person-role {
    position: absolute;
    left: 130px; top: 432px;
    margin: 0;
    font-size: 34px;
    font-weight: 400;
    color: var(--ink);
  }
  .contact {
    position: absolute;
    left: 524px; top: 374px;
    margin: 0;
    font-size: 34px;
    color: var(--ink);
  }
  .contact-line { display: block; height: 58px; }
  .address-band {
    position: absolute;
    left: 0; top: 574px;
    width: 100%; height: 130px;
    background: var(--sky);
  }
  .address {
    position: absolute;
    left: 130px; top: 624px;
    margin: 0;
    font-size: 31px;
    color: var(--paper);
    letter-spacing: 0.3px;
  }
</style>
</head>
<body>
  <main class="card">
    <div class="top-band"></div>

    <div class="brand-mark" aria-hidden="true"></div>
    <h1 class="brand-name">Cedar Gate Rentals</h1>
    <p class="slogan">Your next dream house</p>

    <h2 class="person-name">MARLON</h2>
    <p class="person-role">General Manager</p>

    <address class="contact">
      <span class="contact-line">+1 202 5550147</span>
      <span class="contact-line">marketing@cedargaterentals.com</span>
    </address>

    <div class="address-band"></div>
    <p class="address">82 Linden Street, Apt. 214. New York, NY 10021. Code Post</p>
  </main>
</body>
</html>
```